Ridgeback Gear Depot

Design a new website design for www.ridgebackgeardepot.example,

Target Market(s)

Men & Ladies

Industry/Entity Type

Side X side, ATV Offroad

Coding

Coded - Design and coding required

Number of Pages Required

1 page

```html
<!DOCTYPE html>
<html lang="en">
<head>
<meta charset="utf-8">
<title>Ridgeback Gear Depot</title>
<link href="https://fonts.googleapis.com/css2?family=Poppins:wght@400;500;600;700;800&family=Roboto:wght@400;500;700&display=swap" rel="stylesheet">
<style>
:root{
  --accent:#f4563a;
  --ink:#111;
  --dark:#0d0d0d;
  --muted:#7a7a7a;
  --line:#e6e6e6;
  --grey-band:#e4e4e4;
  --white:#fff;
}
*{box-sizing:border-box;margin:0;padding:0}
html,body{width:1200px;height:4491px;overflow:hidden}
body{position:relative;font-family:Roboto,Arial,sans-serif;color:var(--ink);background:var(--white)}
.abs{position:absolute}
.h{font-family:Poppins,Arial,sans-serif}
/* header */
.topline{left:0;top:0;width:1200px;height:5px;background:var(--dark)}
.logo{left:66px;top:8px;font-family:Poppins,sans-serif;font-weight:600;font-size:28px;line-height:30px;color:var(--ink)}
.search{left:316px;top:30px;width:600px;height:45px;background:#f1f1f1;font-size:13px;color:#999;padding:14px 16px}
.search-btn{left:870px;top:30px;width:46px;height:45px;background:var(--ink)}
.cart{left:970px;top:44px;font-size:13px;font-weight:700}
.login{left:1046px;top:44px;font-size:13px;color:#555}
.brandbar{left:0;top:101px;width:1200px;height:61px;background:#000;display:flex;justify-content:center;align-items:center;gap:44px}
.brandbar span{color:#fff;font-family:Poppins,sans-serif;font-weight:600;font-size:13px;letter-spacing:.5px}
/* hero */
.hero{left:0;top:162px;width:1200px;height:705px;background:radial-gradient(circle at 8% 10%,#4a1610 0,#1a1111 22%,#151515 55%,#0f0f0f 100%)}
.hero-photo{left:330px;top:162px;width:870px;height:705px;background:radial-gradient(ellipse at 60% 55%,#8a8a86 0,#55534f 30%,#2a2827 60%,rgba(20,20,20,0) 80%)}
.kicker{font-family:Poppins,sans-serif;font-weight:600;font-size:12px;letter-spacing:2px;color:var(--accent)}
.hero-title{left:148px;top:402px;font-family:Poppins,sans-serif;font-weight:700;font-size:54px;line-height:56px;color:#fff}
.hero-text{left:148px;top:536px;width:420px;font-size:14px;line-height:21px;color:#ddd}
.btn-accent{background:var(--accent);color:#fff;font-weight:700;font-size:13px;display:flex;align-items:center;justify-content:center;gap:10px}
.social-dot{width:12px;height:12px;border-radius:50%;background:#fff}
/* features */
.greyband{left:0;top:867px;width:1200px;height:532px;background:var(--grey-band)}
.features{left:66px;top:792px;width:1068px;height:206px;background:#fff;display:flex}
.feature{flex:1;border-right:1px solid var(--line);text-align:center;padding-top:30px}
.feature:last-child{border-right:none}
.feature h3{font-family:Poppins,sans-serif;font-weight:600;font-size:20px;margin-top:14px}
.feature p{font-size:13px;color:var(--muted);margin-top:14px}
.promo{display:flex;flex-direction:column;align-items:flex-end;padding:60px 34px 0 0}
.promo h2{font-family:Poppins,sans-serif;font-weight:600;font-size:34px;color:#fff}
.promo p{font-size:13px;color:#eee;margin-top:10px}
.promo .btn-accent{margin-top:16px;width:108px;height:34px}
/* products */
.section-kicker{width:1200px;text-align:center;font-family:Poppins,sans-serif;font-weight:600;font-size:12px;letter-spacing:2px;color:var(--accent)}
.section-title{width:1200px;text-align:center;font-family:Poppins,sans-serif;font-weight:600;font-size:36px}
.card{background:#fff;box-shadow:0 2px 12px rgba(0,0,0,.08);display:flex;flex-direction:column;align-items:center;text-align:center;padding:0 8px}
.card .pic{width:228px;height:220px;margin-top:14px;background:radial-gradient(circle,#8b776a 0,#b3a49a 35%,#fff 70%)}
.card h4{font-family:Poppins,sans-serif;font-weight:600;font-size:13.5px;line-height:18px;margin-top:12px}
.price{font-size:12px;color:var(--accent);margin-top:10px}
.price s{color:#bbb;margin-right:4px}
.price u{font-weight:700}
.add{margin-top:16px;background:#000;color:#fff;font-weight:700;font-size:13px;padding:9px 20px}
.sale{width:38px;height:38px;border-radius:50%;background:var(--accent);color:#fff;font-size:11px;font-weight:700;display:flex;align-items:center;justify-content:center;position:absolute;top:-4px;right:12px}
/* flash */
.flash-band{left:0;top:2075px;width:1200px;height:630px;background:linear-gradient(135deg,#2d322c,#454a3e 50%,#2a2e28)}
.flash-box{left:80px;top:2166px;width:398px;height:448px;background:#fff}
.count{font-family:Poppins,sans-serif;font-weight:600;font-size:46px;color:var(--accent);text-align:center;width:80px}
.count small{display:block;font-family:Roboto,sans-serif;font-weight:400;font-size:13px;margin-top:-4px}
/* testimonial */
.testi-band{left:0;top:3383px;width:1200px;height:445px;background:linear-gradient(90deg,#1a1a1a 0,#2c2c2c 40%,#6e6e6e 75%,#d8d8d8 100%)}
.tcard{background:#fff;padding:30px 28px}
.stars{color:var(--accent);font-size:16px;letter-spacing:6px}
.tcard p{font-size:13px;line-height:22px;color:#999;margin-top:20px}
.avatar{width:64px;height:64px;border-radius:50%;background:#9aa3ab}
/* partner */
.partner-band{left:96px;top:4044px;width:1008px;height:89px;background:#000;display:flex;justify-content:space-around;align-items:center}
.partner-band span{color:#fff;font-family:Poppins,sans-serif;font-weight:700;font-size:22px}
/* footer */
.footer{left:0;top:4165px;width:1200px;height:326px;background:#000;color:#fff}
.flabel{font-family:Poppins,sans-serif;font-weight:600;font-size:12px;letter-spacing:2px;color:var(--accent)}
.flink{font-size:13px;display:flex;align-items:center;gap:8px}
.flink i{width:10px;height:10px;border-radius:50%;background:var(--accent)}
.pay{width:28px;height:18px;border-radius:3px;background:#3d5bd6}
</style>
</head>
<body>
<div class="abs topline"></div>
<div class="abs logo">RIDGEBACK<br>GEAR<br>Depot</div>
<div class="abs search">What are you looking for ...</div>
<div class="abs search-btn">
  <svg width="46" height="45" viewBox="0 0 46 45"><circle cx="22" cy="21" r="6" fill="none" stroke="#fff" stroke-width="2"/><line x1="26" y1="25" x2="30" y2="29" stroke="#fff" stroke-width="2"/></svg>
</div>
<div class="abs cart">$0.00 &#128722;</div>
<div class="abs login">&#9679; Login</div>

<nav class="abs brandbar">
  <span>IRONVALE</span><span>KESTREL</span><span>NORTHTRAK</span><span>TAMURA</span><span>HOSHIDO</span><span>CROSSMARK</span>
</nav>

<section class="abs hero"></section>
<div class="abs hero-photo" role="img" aria-label="Grey and orange side-by-side utility vehicle on dark background"></div>
<div class="abs kicker" style="left:148px;top:372px">HIGH QUALITY</div>
<h1 class="abs hero-title">ATV<br>PRODUCTS</h1>
<p class="abs hero-text">Lorem ipsum dolor sit amet, consectetur adipiscing elit. Ut elit tellus, luctus nec ullamcorper mattis, pulvinar dapibus leo.</p>
<a class="abs btn-accent" style="left:148px;top:614px;width:155px;height:42px">Shop Now <span>&rarr;</span></a>
<div class="abs social-dot" style="left:86px;top:479px"></div>
<div class="abs social-dot" style="left:86px;top:508px"></div>
<div class="abs social-dot" style="left:86px;top:540px"></div>

<div class="abs greyband"></div>
<div class="abs features">
  <div class="feature">
    <svg width="60" height="66" viewBox="0 0 60 66"><path d="M30 4 L54 12 V32 C54 48 42 58 30 62 C18 58 6 48 6 32 V12 Z" fill="none" stroke="var(--accent)" stroke-width="4"/><path d="M19 33 L27 41 L42 24" fill="none" stroke="var(--accent)" stroke-width="4"/></svg>
    <h3>Trusted Partners</h3><p>Rate Customer 4.7</p>
  </div>
  <div class="feature">
    <svg width="72" height="60" viewBox="0 0 72 60"><rect x="4" y="6" width="56" height="38" rx="4" fill="none" stroke="var(--accent)" stroke-width="3"/><rect x="12" y="16" width="56" height="38" rx="4" fill="#fff" stroke="var(--accent)" stroke-width="3"/><circle cx="36" cy="35" r="5" fill="none" stroke="var(--accent)" stroke-width="3"/><circle cx="44" cy="35" r="5" fill="none" stroke="var(--accent)" stroke-width="3"/></svg>
    <h3>Secure Payment</h3><p>Many Payment Gateway Support</p>
  </div>
  <div class="feature">
    <svg width="66" height="62" viewBox="0 0 66 62"><path d="M12 32 V26 A21 21 0 0 1 54 26 V32" fill="none" stroke="var(--accent)" stroke-width="3"/><rect x="6" y="28" width="10" height="16" rx="3" fill="none" stroke="var(--accent)" stroke-width="3"/><rect x="50" y="28" width="10" height="16" rx="3" fill="none" stroke="var(--accent)" stroke-width="3"/><circle cx="33" cy="30" r="11" fill="none" stroke="var(--accent)" stroke-width="3"/><path d="M28 30 L32 34 L38 26" fill="none" stroke="var(--accent)" stroke-width="3"/></svg>
    <h3>27/7 Support</h3><p>We Always Ready For You</p>
  </div>
</div>

<div class="abs promo" style="left:75px;top:1083px;width:687px;height:262px;background:linear-gradient(160deg,#6b7480,#8a7f73 55%,#c07c44)" role="img" aria-label="Off-road vehicle jumping at sunset">
  <h2>New Arrivals</h2><p>Discount up to 20% for Early Down Payment</p><a class="btn-accent">Buy Now !</a>
</div>
<div class="abs promo" style="left:780px;top:1083px;width:345px;height:262px;background:linear-gradient(160deg,#56606b,#3d3a35 60%,#5a4d3d);padding-right:32px" role="img" aria-label="Green side-by-side vehicle parked on dirt">
  <h2>On Sale</h2><p>Discount 20% for Repair</p><a class="btn-accent">Shop Now</a>
</div>

<div class="abs section-kicker" style="left:0;top:1483px">LATEST PRODUCT</div>
<h2 class="abs section-title" style="left:0;top:1508px">New Arrival Product</h2>

<div class="abs card" style="left:75px;top:1570px;width:248px;height:420px"><span class="sale">Sale!</span><div class="pic" role="img" aria-label="Gear reduction set"></div><h4>Razorline, Turbo, Ridgerunner, Marshal, or Dart 19% Gear Reduction</h4><div class="price"><s>$700.00</s><u>$649.99</u></div><a class="add">Add to cart</a></div>
<div class="abs card" style="left:344px;top:1570px;width:248px;height:420px"><span class="sale">Sale!</span><div class="pic" role="img" aria-label="Gear with two bearing rings"></div><h4>Northtrak Turf Mode Delete / Razorline 900, 1000 / Ridgerunner 900, 1000 / Marshal</h4><div class="price"><s>$320.00</s><u>$299.99</u></div><a class="add">Add to cart</a></div>
<div class="abs card" style="left:609px;top:1570px;width:248px;height:420px"><div class="pic" role="img" aria-label="Clutch housing with springs"></div><h4>Reduction 420/500/520 Primary 60% Homestead Frontier Canyon Overseer</h4><div class="price">$699.99</div><a class="add">Add to cart</a></div>
<div class="abs card" style="left:875px;top:1570px;width:250px;height:420px"><div class="pic" role="img" aria-label="Double gear assembly"></div><h4>Homestead Frontier Canyon Overseer</h4><div class="price">$399.99</div><a class="add">Add to cart</a></div>

<section class="abs flash-band" role="img" aria-label="Blurred off-road trail background"></section>
<div class="abs flash-box">
  <svg class="abs" style="left:46px;top:96px" width="32" height="48" viewBox="0 0 32 48"><path d="M20 2 L4 28 H16 L10 46 L28 18 H16 Z" fill="none" stroke="var(--accent)" stroke-width="2"/></svg>
  <div class="abs h" style="left:93px;top:82px;font-size:35px;font-weight:500">Flash Deal</div>
  <p class="abs" style="left:93px;top:144px;width:280px;font-size:13px;line-height:20px;color:var(--muted)">Get Super Offer Only 2 Hours. Discount Up to 50% Just For You.</p>
  <a class="abs" style="left:101px;top:209px;width:244px;height:42px;background:#000;color:#fff;font-weight:700;font-size:13px;display:flex;align-items:center;justify-content:center">More Info Flash Deal</a>
  <div class="abs count" style="left:33px;top:282px">20<small>Hours</small></div>
  <div class="abs count" style="left:159px;top:282px">37<small>Minutes</small></div>
  <div class="abs count" style="left:285px;top:282px">23<small>Seconds</small></div>
</div>
<div class="abs card" style="left:508px;top:2166px;width:296px;height:448px;box-shadow:none"><div class="pic" style="width:270px;height:280px" role="img" aria-label="Gear reduction set"></div><h4>Razorline, Turbo, Ridgerunner, Marshal, or Dart 19% Gear Reduction</h4><div class="price"><s>$700.00</s><u>$649.99</u></div><a class="add">Add to cart</a></div>
<div class="abs card" style="left:823px;top:2166px;width:295px;height:448px;box-shadow:none"><span class="sale">Sale!</span><div class="pic" style="width:270px;height:280px" role="img" aria-label="Gear with two bearing rings"></div><h4>Northtrak Turf Mode Delete / Razorline 900, 1000 / Ridgerunner 900, 1000 / Marshal</h4><div class="price"><s>$320.00</s><u>$299.99</u></div><a class="add">Add to cart</a></div>
<span class="abs sale" style="left:773px;top:2162px">Sale!</span>

<div class="abs section-kicker" style="left:0;top:2788px">ON SALE PRODUCT</div>
<h2 class="abs section-title" style="left:0;top:2813px">Best Seller Product</h2>

<div class="abs card" style="left:75px;top:2878px;width:248px;height:418px"><span class="sale">Sale!</span><div class="pic" role="img" aria-label="Gear reduction set"></div><h4>Razorline, Turbo, Ridgerunner, Marshal, or Dart 19% Gear Reduction</h4><div class="price"><s>$700.00</s><u>$649.99</u></div><a class="add">Add to cart</a></div>
<div class="abs card" style="left:344px;top:2878px;width:248px;height:418px"><span class="sale">Sale!</span><div class="pic" role="img" aria-label="Gear with two bearing rings"></div><h4>Northtrak Turf Mode Delete / Razorline 900, 1000 / Ridgerunner 900, 1000 / Marshal</h4><div class="price"><s>$320.00</s><u>$299.99</u></div><a class="add">Add to cart</a></div>
<div class="abs card" style="left:609px;top:2878px;width:248px;height:418px"><div class="pic" role="img" aria-label="Clutch housing with springs"></div><h4>Reduction 420/500/520 Primary 60% Homestead Frontier Canyon Overseer</h4><div class="price">$699.99</div><a class="add">Add to cart</a></div>
<div class="abs card" style="left:875px;top:2878px;width:250px;height:418px"><div class="pic" role="img" aria-label="Double gear assembly"></div><h4>Homestead Frontier Canyon Overseer</h4><div class="price">$399.99</div><a class="add">Add to cart</a></div>

<section class="abs testi-band" role="img" aria-label="Dusty off-road riding scene"></section>
<div class="abs kicker" style="left:89px;top:3522px;color:#fff">TESTIMONIAL</div>
<h2 class="abs h" style="left:89px;top:3548px;color:#fff;font-size:36px;font-weight:600">What They Say</h2>
<p class="abs" style="left:89px;top:3610px;width:300px;font-size:13px;line-height:20px;color:#ddd">Lorem ipsum dolor sit amet, consectetur adipiscing elit. Ut elit tellus, luctus nec ullamcorper mattis, pulvinar dapibus leo.</p>

<div class="abs tcard" style="left:410px;top:3457px;width:350px;height:296px">
  <div class="stars">&#9733;&#9733;&#9733;&#9733;&#9733;</div>
  <p>Egestas sit eget platea justo sodales pulvinar tristique eleifend nam libero. Sagittis natoque sed suspendisse consequat semper rhoncus habitasse class.</p>
  <div class="abs avatar" style="left:28px;top:198px" role="img" aria-label="Customer portrait"></div>
  <div class="abs h" style="left:112px;top:208px;font-weight:600;font-size:15px">Dale Brooks</div>
  <div class="abs" style="left:112px;top:232px;font-size:12px;color:var(--muted)">Biker</div>
  <div class="abs h" style="right:26px;top:186px;font-size:80px;font-weight:800;color:var(--accent);line-height:80px">&rdquo;</div>
</div>
<div class="abs tcard" style="left:776px;top:3457px;width:351px;height:296px">
  <div class="stars">&#9733;&#9733;&#9733;&#9733;&#9733;</div>
  <p>Egestas sit eget platea justo sodales pulvinar tristique eleifend nam libero. Sagittis natoque sed suspendisse consequat semper rhoncus habitasse class.</p>
  <div class="abs avatar" style="left:28px;top:198px" role="img" aria-label="Customer portrait"></div>
  <div class="abs h" style="left:112px;top:208px;font-weight:600;font-size:15px">Dale Brooks</div>
  <div class="abs" style="left:112px;top:232px;font-size:12px;color:var(--muted)">Biker</div>
  <div class="abs h" style="right:26px;top:186px;font-size:80px;font-weight:800;color:var(--accent);line-height:80px">&rdquo;</div>
</div>

<div class="abs section-kicker" style="left:0;top:3902px">PARTNER</div>
<h2 class="abs section-title" style="left:0;top:3927px">Awesome Partner</h2>
<p class="abs" style="left:0;top:3992px;width:1200px;text-align:center;font-size:13px;color:var(--muted)">Netus turpis curabitur purus massa non feugiat dictum nostra pretium. Quis id augue phasellus posuere efficitur justo potenti nascetur.</p>
<div class="abs partner-band"><span>CROSSMARK</span><span>IRONVALE</span><span>KESTREL</span><span>NORTHTRAK</span><span>TAMURA</span></div>

<footer class="abs footer">
  <div class="abs h" style="left:75px;top:78px;font-size:18px;font-weight:600;line-height:20px">RIDGEBACK<br>GEAR DEPOT</div>
  <div class="abs" style="left:75px;top:130px;width:60px;height:2px;background:var(--accent)"></div>
  <div class="abs social-dot" style="left:83px;top:166px"></div>
  <div class="abs social-dot" style="left:117px;top:166px"></div>
  <div class="abs social-dot" style="left:152px;top:166px"></div>
  <div class="abs flabel" style="left:323px;top:74px">PHONE</div>
  <div class="abs" style="left:323px;top:104px;font-size:12px">+(00)55-0148-2290</div>
  <div class="abs flabel" style="left:323px;top:137px">EMAIL US</div>
  <div class="abs" style="left:323px;top:166px;font-size:12px">support@ridgebackgeardepot.example</div>
  <div class="abs" style="left:323px;top:196px;width:70px;height:2px;background:var(--accent)"></div>
  <div class="abs flink" style="left:541px;top:78px"><i></i>Privacy Policy</div>
  <div class="abs flink" style="left:541px;top:101px"><i></i>Returns Policy</div>
  <div class="abs flink" style="left:541px;top:124px"><i></i>Contact</div>
  <div class="abs flink" style="left:541px;top:147px"><i></i>FAQS</div>
  <div class="abs" style="left:788px;top:0;width:1px;height:240px;background:#333"></div>
  <div class="abs" style="left:818px;top:75px;width:269px;height:35px;background:#fff;color:#999;font-size:12px;padding:10px 14px">Name</div>
  <div class="abs btn-accent" style="left:818px;top:124px;width:269px;height:34px">SIGNUP NOW</div>
  <div class="abs" style="left:96px;top:267px;font-size:12px;color:#ccc">&copy; 2024 Ridgeback Gear Depot. All Rights Reserved.</div>
  <div class="abs" style="left:891px;top:264px;display:flex;gap:6px">
    <span class="pay"></span><span class="pay" style="background:#fff"></span><span class="pay" style="background:#fff"></span><span class="pay"></span><span class="pay" style="background:#1a1f71"></span><span class="pay" style="background:#6b3fd4"></span><span class="pay" style="background:#fff"></span>
  </div>
</footer>
</body>
</html>
```